Book a car wash

The app will have a logo, contact details and address
It will then lead you to booking a service from list
The customer will have a date, day and time

Booking - There are two types of times arrival is the main - day, date, time, service, payment. Each car takes and average of 1.5 hours

Pay by qlink or fundly or merchant

List of services
Bronze $25
Silver $40
Gold $55
Leather Plus $90
Diamond $100
Ruby $100
Standard Vehicle $0
Larger Vehicle & 4wd $10

Target Market(s)

Professionals with time issues
Parents with time management concerns

Industry/Entity Type

It Service

Requirements
Must have
• Logo
Menu list
Payment system
Address and contact details
Basement CarPark - Wexley Court Shopping Centre
Tarvin rd, Claremont
0493520741
Nice to have
• Big fonts and step by step process
Should not have
• No cars or washing items i.e. sponges

```html
<!DOCTYPE html>
<html lang="en">
<head>
<meta charset="utf-8">
<title>Park &amp; Shine – Book a Car Wash</title>
<link href="https://fonts.googleapis.com/css2?family=Open+Sans:ital,wght@0,400;0,600;0,700;1,400&display=swap" rel="stylesheet">
<style>
  :root{
    --white:#ffffff;
    --ink:#1c2a3a;
    --band:#12305a;
    --body-top:#1f4c6b;
    --body-bottom:#0e2236;
    --field:#0c1f34;
    --field-line:#3a5d7c;
    --cyan:#36c6e8;
    --soft:#d6e3ee;
    --green-top:#8fd13a;
    --green-bottom:#5ea31c;
    --chip:#f4f6f8;
    --chip-text:#2b4a7a;
    --nav-text:#333b45;
    --accent:#e8862a;
  }
  *{box-sizing:border-box;margin:0;padding:0}
  html,body{width:1200px;height:2248px;overflow:hidden;background:#101b28}
  body{font-family:"Open Sans",Arial,sans-serif;color:var(--white)}
  .screen{position:relative;width:1200px;height:2248px}

  .app-header{position:absolute;left:0;top:0;width:1200px;height:330px;background:var(--white);
    display:flex;align-items:center;justify-content:space-between;padding:0 70px}
  .brand{display:flex;align-items:center;gap:22px}
  .brand-dot{width:58px;height:58px;border-radius:50%;background:var(--accent)}
  .brand-name{font-weight:700;font-size:52px;color:var(--ink)}
  .profile-icon{width:160px;height:160px}

  .title-band{position:absolute;left:0;top:330px;width:1200px;height:210px;background:var(--band);
    display:flex;align-items:center;justify-content:center;gap:56px;border-bottom:4px solid #0a1c33}
  .title-band h1{font-size:62px;font-weight:600}
  .car-icon{width:110px;height:84px}

  .booking{position:absolute;left:0;top:540px;width:1200px;height:1464px;
    background:radial-gradient(ellipse at 50% 0%,var(--body-top) 0%,var(--body-bottom) 80%)}
  .welcome{position:absolute;left:110px;top:70px;width:990px}
  .welcome h2{font-size:54px;font-weight:400;margin-bottom:22px}
  .welcome .intro{font-size:32px;line-height:46px;color:var(--cyan)}
  .welcome .note{font-size:31px;color:var(--soft);margin-top:40px}
  .divider{position:absolute;left:96px;width:1002px;height:2px;background:rgba(255,255,255,0.12);top:510px}

  .field{position:absolute;height:104px;background:var(--field);border:2px solid var(--field-line);
    border-radius:6px;display:flex;align-items:center;padding:0 30px;font-style:italic;font-size:30px;color:var(--white)}
  .field.select::after{content:"";position:absolute;right:30px;top:43px;border-left:13px solid transparent;
    border-right:13px solid transparent;border-top:16px solid var(--white)}
  .f-day{left:96px;top:570px;width:478px}
  .f-service{left:620px;top:570px;width:478px}
  .f-date{left:96px;top:720px;width:315px}
  .f-month{left:440px;top:720px;width:315px}
  .f-time{left:783px;top:720px;width:315px}

  .pay-heading{position:absolute;left:96px;top:890px;width:1002px;display:flex;align-items:center;gap:24px;
    font-size:32px;color:var(--soft);letter-spacing:1px}
  .pay-heading::before,.pay-heading::after{content:"";flex:1;height:2px;background:rgba(255,255,255,0.15)}

  .pay-options{position:absolute;left:0;top:988px;width:1200px;display:flex;justify-content:center;gap:36px}
  .pay-chip{width:132px;height:74px;background:var(--chip);border-radius:6px;display:flex;align-items:center;
    justify-content:center;font-size:23px;font-weight:700;color:var(--chip-text)}

  .book-button{position:absolute;left:130px;top:1128px;width:968px;height:96px;border:none;border-radius:8px;
    background:linear-gradient(var(--green-top),var(--green-bottom));color:var(--white);
    font-family:"Open Sans",Arial,sans-serif;font-size:34px;font-weight:700;letter-spacing:0.5px}

  .tab-bar{position:absolute;left:0;top:2004px;width:1200px;height:244px;background:var(--white);
    display:flex;justify-content:space-around;align-items:center;padding:0 20px}
  .tab{display:flex;flex-direction:column;align-items:center;gap:16px;width:250px}
  .tab svg{width:100px;height:92px}
  .tab span{font-size:30px;color:var(--nav-text);letter-spacing:0.5px}
</style>
</head>
<body>
<div class="screen">

  <header class="app-header">
    <div class="brand">
      <span class="brand-dot"></span>
      <span class="brand-name">Park &amp; Shine</span>
    </div>
    <svg class="profile-icon" viewBox="0 0 100 100" aria-label="My profile">
      <circle cx="50" cy="34" r="20" fill="#2c2f34"/>
      <path d="M12 96c0-24 16-38 38-38s38 14 38 38z" fill="#2c2f34"/>
    </svg>
  </header>

  <section class="title-band">
    <svg class="car-icon" viewBox="0 0 120 90" aria-hidden="true">
      <path d="M22 40l12-26h52l12 26" fill="none" stroke="#fff" stroke-width="8" stroke-linejoin="round"/>
      <rect x="10" y="38" width="100" height="32" rx="8" fill="#fff"/>
      <rect x="16" y="66" width="20" height="18" rx="4" fill="#fff"/>
      <rect x="84" y="66" width="20" height="18" rx="4" fill="#fff"/>
      <circle cx="30" cy="54" r="7" fill="#12305a"/>
      <circle cx="90" cy="54" r="7" fill="#12305a"/>
    </svg>
    <h1>Book a Car Wash</h1>
  </section>

  <main class="booking">
    <div class="welcome">
      <h2>Welcome note Title</h2>
      <p class="intro">This is Pixelbox's version of Lorem Ipsum. Proin gravida nibh vel velit auctor aliquet. Aenean sollicitudin, lorem quis bibendum auctor, nisi elit consequat ipsum, nec sagittis sem nibh id elit.</p>
      <p class="note">Each car takes and average of 1.5 hours</p>
    </div>
    <div class="divider"></div>

    <div class="field f-day">Select a day..</div>
    <div class="field f-service">Select Services</div>
    <div class="field select f-date">Date</div>
    <div class="field select f-month">Month</div>
    <div class="field select f-time">Time</div>

    <div class="pay-heading">CHOOSE YOUR PAYMENT OPTION</div>
    <div class="pay-options">
      <div class="pay-chip">Cardora</div>
      <div class="pay-chip">Veyra</div>
      <div class="pay-chip">Paydrift</div>
      <div class="pay-chip">Orbix</div>
      <div class="pay-chip">Glimpay</div>
    </div>

    <button class="book-button">BOOK CAR WASH</button>
  </main>

  <nav class="tab-bar">
    <div class="tab">
      <svg viewBox="0 0 110 100" aria-hidden="true">
        <path d="M20 30l50-18 8 18z" fill="#2c2f34"/>
        <rect x="14" y="30" width="80" height="60" rx="6" fill="#2c2f34"/>
        <rect x="70" y="50" width="30" height="20" rx="4" fill="#2c2f34" stroke="#fff" stroke-width="3"/>
        <circle cx="80" cy="60" r="4" fill="#fff"/>
      </svg>
      <span>MY ACCOUNT</span>
    </div>
    <div class="tab">
      <svg viewBox="0 0 110 100" aria-hidden="true">
        <path d="M55 30L20 18 8 34l35 12zM55 30l35-12 12 16-35 12z" fill="none" stroke="#2c2f34" stroke-width="6" stroke-linejoin="round"/>
        <path d="M22 42v34l33 14 33-14V42L55 54z" fill="#2c2f34"/>
      </svg>
      <span>OFFERS</span>
    </div>
    <div class="tab">
      <svg viewBox="0 0 110 100" aria-hidden="true">
        <path d="M55 90C20 64 10 48 10 32 10 18 21 8 34 8c10 0 17 6 21 13 4-7 11-13 21-13 13 0 24 10 24 24 0 16-10 32-45 58z" fill="#2c2f34"/>
      </svg>
      <span>FAVOURITES</span>
    </div>
    <div class="tab">
      <svg viewBox="0 0 110 100" aria-hidden="true">
        <circle cx="55" cy="50" r="44" fill="#2c2f34"/>
        <circle cx="58" cy="28" r="6" fill="#fff"/>
        <path d="M46 44h16l-6 30h8" fill="none" stroke="#fff" stroke-width="8" stroke-linejoin="round"/>
      </svg>
      <span>ABOUT</span>
    </div>
  </nav>

</div>
</body>
</html>
```